International trading company needs banner designs for university careers fairs. Additional work to

Description
Our company, Meridale Capital, operates in the finance industry. We trade numerous financial instruments across the globe. We focus on futures, options, etfs and are currently expanding into the exciting area of cryptocurrencies. A main focus of ours is to use a systematic and quantitative approach to trading to develop and refine trading strategies that are relatively low risk in nature, but are scalable and provide positive returns. We work hard, we push each other to achieve great results. But at the same time we really enjoy each other’s company and share a relaxed atmosphere at work. Our website is http://www.meridalecapital.com.au/. Meridale will be attending university careers fairs and expos in coming months to attract the very best talent there is for graduate trading roles as well as graduate developer roles. As such, we require our booth to look professional. We want to convey our message that a career with us is exciting, rewarding, but also challenging. We aim to nurture talent and hope to provide the tools necessary to strive in a career in trading.

We have 3 aspects to our booth concept. But for this designer contest, we will focus on 1 of those projects. When we decide on one designer, we hope they will be willing to work one on one on the other 2 projects. On top of this contest, we are willing to pay $250 for the additional 2 projects, one of which is quite simple in design brief, the other will allow the designer the flare to be creative. It is important to note that all three concepts need to be cohesive. Each concept should complement the other in colour as well as message.

For the entire project to be finished, we are a little rushed on time and would require completion of all three concepts by February 2nd.

We will only require soft copy files so we can manage the print ourselves. We can accept a vector, eps or ai file.

For this contest project, the design concept is a pull-up banner. We will have 3 pull-up banners each with slightly different messages.

We have attached pictures to help inspire the designer. Also, we have attached company logo (a unicorn) and name, along with varying colour vectors.

Meridale Capital’s primary colours are black, green and white. We would like all 3 banners to be in the same scheme. But we are happy to see slightly different variations in design options on the colour scheme. We do feel that green writing on black background would look the sharpest and have the most impact. We could be wrong though and are fine to see different designs.

The banner dimensions will be 85cm wide x 210cm tall. So there is room on the banner to deliver an exciting, yet professional message.

Preliminary Pull-up Banner ideas
We are not designers, we are open to you, the designer, using your creative flare to design 3 sharp looking banners. We do have a rough idea of the direction of each banner though.

Banner 1 – A company inspired banner. We would like our company name, our logo (prominent!) and beneath it 3 to 4 words that describe what we’re about. For example, Challenging, Rewarding, Passionate, Entrepreneurial, Focused, Collaborative, Innovative, Systematic, Strategic. Happy for the designer to take control here.

For the rest of the banner we are open to design. Potentially a picture taken from our website that is reflective of our culture – which is relaxed, hard-working, collaborative, rewarding.

It doesn’t need to be too busy or cluttered, so no need to throw in designs that aren’t really consistent with us.

Banner 2 – A trader inspired banner. This is more designed to attract graduates interested in a career in trading. Include meridale name and logo. Maybe include a question for the students... Something like,
“Want to be challenged?
Want to strategise?
Want to be rewarded?
Become a trader!”
Doesn’t have to be straight angles, can be on an angle – designer free reign here. Also we can have different sentences, words. Up to the designer. We would like to include something that would attract a trader’s mind, something visual, like a trading chart. See attached pictures for trading chart examples.

Somewhere on the banner we can mention Graduate Trader Program, please contact us at careers@meridalecapital.com.au. Phone number below it (02) 7156 4830.

Banner 3 - A developer inspired banner. This is more designed to attract graduates interested in a career in developing. Include meridale name and logo

Put the following pitch on the banner and fill the rest of the space with designs and pictures. No fixed layout required here.

Good at problem solving? Obsessed with creating quality software? Love working with numbers? Do you speak programming language? Want to face fresh challenges each day?

On the banner we can mention Graduate Software Engineer Program, please contact us at careers@meridalecapital.com.au. Phone number below it (02) 7156 4830.

Additionally to the above 3 banners, we had an idea of including random words across the banners in random sizes and boldness. We’re not sure how this would appear so we would like to see a couple designs on this. We thought we could have a top tier of buzz words that should be more prominent with the second tier buzzwords in smaller size. Two design types - randomly displayed, secondly a bit more structured. Can decide what looks best when we receive design. Words below. We don’t have to include all of these words, whatever a good design lends itself to. Words should only be in green, black or white - consistent with our company scheme.

Top Tier Buzzwords
Trading
Cryptocurrency
Options
Market making
Trading
Bitcoin
Derivatives
ETF
Futures
Volatility
Arbitrage
Technology
HFT
Hedging

Second Tier Buzzwords
R&K 400
QMB 300
VLZ
DWT
QMB
FX
Bid
Offer
Margining
Long
Short
Spot
Position
Tolvar
Brimo
Wel Daro
WDI
GGI
Buy
Sell
Delta
Gamma
Vega
Theta
Skew
Straddle
Call

Once we have selected the designer, we are keen that they would complete another 2 projects for us. The other 2 projects are as follows:
• A double sided A5 flyer design – This should provide more information about what Meridale can offer the students as a career and a workplace. We will also give a small amount of detail about the graduate program.
• Table Cloth design – At each exhibition we receive a table at our booth. We would like to have a logo laden table cloth that will look professional

We would like the design scheme to flow neatly from the banners to the flyers to the table cloth. So the colours are consistent and our general tone/message is also consistent.

We have attached pictures that should help the designer. Included pictures of pull-up banners, pictures of student careers fairs, flyers, table cloth dimensions, Meridale’s logos and colour vectors.

Preliminary Double sided A5 Flyer ideas.

We would need two designs – a trader design and a developer design.

Art file to be supplied PDF file with trim marks & 3mm bleed

With the flyer we would like to add a little more information about Meridale on the front page (which should be the same for the trader flyer and the developer flyer). On the back page we would be a little more detailed in the graduate program. Give dates, the onboarding process, rough program details/info.

Front Page – Include Meridale name, logo. Explanation of who we are - proprietary trading firm, using our own capital to trade financial instruments around the world. We trade futures, options, etfs and cryptocurrencies (can make more elaborate).

To make it sound interesting we’d like to explain potential for growth in certain markets. So something along the lines, of “We are seeing rapid expansion in certain markets. At meridale we are always looking for new strategies and talent to expand our already growing presence. Working with Meridale, you’ll get exposure and experience on all of these exciting markets which will greatly benefit you in your career progression” (Doesn’t need to be word for word)

We’d also like to mention some of the perks of working with us:
daily lunch provided
cafe coffee
 breakfast/snacks
 casual attire
 cash bonus half yearly
 competitive rates
 team dinners
 gym membership
 company trips
We’d like to use consistent colour schemes with our company, Black and Green. Some white could work in there. But not a necessity.
The designer can feel free to add in some sharp looking images.

Back Page Trader Flyer - We would like to give some more info on the positives of the trader program. We’re mainly focusing on the strengths of the program here – listed below.
• 1 on 1 training
• In-depth theory classes with practical applications
• Experienced traders providing the training
• Live trading within 3 months
• Ongoing mentoring
• Exposure to different markets/strategies
• Placed onto products that best suit their strengths
• Simulated trader training based on actual events

We should also add contact details for students to apply to.
For more information on the Graduate Trader Program
contact us at careers@meridalecapital.com.au.
Phone number (02) 7156 4830.

OR

To apply please send through your CV and academic transcript to careers@meridalecapital.com.au

We would also want this to look quite sharp, so adding in a trading graph could make it look exciting and attractive.

Back Page Developer Flyer
• 1 on 1 mentoring by senior software engineers
• Full SDLC exposure
• Extremely agile environment
• Direct interaction with business and stakeholders
• Multiple career paths for future growth

For more information on the Graduate Software Engineer Program
Contact us at careers@meridalecapital.com.au.

OR

Preliminary table cloth ideas.
We would need two designs before choosing one.

First design is a very simple design that would look professional. A plain black design with MERIDALE on the front in Green.

The second design is plain black, MERIDALE on the front in Green, similar to above. But we’d also like to see the words mentioned above in the top tier and second tier randomly across the table cloth. In different sizes and weightings.
We’ll see which design looks the best and choose one.

References to see the products we’d be using:
https://brontelsigns.com.au/products/pull-up-banners
https://www.quorvelprint.com.au/lpt/flyers-sizes.aspx?mk=flyers+design&rd=1
https://www.tallowbanners.com.au/outdoor/custom-table-throws/loose-printed-table-throws.html

Target Market(s)

University Graduates in IT, Engineering, Maths, Sciences, Business that would be interested in a career of trading financial instruments including cryptocurrency, options, futures, ETFs. We are also targeting developers in the same space.

Industry/Entity Type

Finance

Font styles to use
Serif
Sans Serif

Colors
00a990
ffffff
000000
33b8a4
1b1b1b

Requirements
Must have
• Cohesion between banners and other project work.
• Clear message coming through
• Professional look
• Eye catching
• Attractive
• Colour schemes must work
Should not have
• Must not be boring. We are looking to project our company image. We are not boring so we want to see some creative flare. But we are also a professional firm so our designs must be sharp.

```html
<!DOCTYPE html>
<html lang="en">
<head>
<meta charset="utf-8">
<title>Meridale Capital – Pull-up Banner</title>
<link rel="stylesheet" href="https://fonts.googleapis.com/css2?family=Open+Sans:wght@300;400;700;800&display=swap">
<style>
  :root {
    --teal: #00a990;
    --teal-light: #33b8a4;
    --teal-dark: #079a82;
    --ink: #1b1b1b;
    --black: #000000;
    --white: #ffffff;
    --stage: #e9eaec;
    --rule: #8fd3c7;
    --photo-top: #f4f5f6;
    --photo-mid: #b9bcc0;
    --photo-low: #5d6066;
  }
  * { margin: 0; padding: 0; box-sizing: border-box; }
  html, body {
    width: 1200px; height: 1200px; overflow: hidden;
    background: var(--stage);
    font-family: "Open Sans", Arial, sans-serif;
  }
  .canvas { position: relative; width: 1200px; height: 1200px; }
  .banner {
    position: absolute; left: 370px; top: 30px;
    width: 422px; height: 1045px;
    transform: scale(1.0905); transform-origin: 0 0;
    background: var(--white); overflow: hidden;
  }
  .banner-art { position: absolute; inset: 0; width: 422px; height: 1045px; }
  .brand-mark {
    position: absolute; left: 171px; top: 15px;
    width: 80px; height: 80px; border-radius: 50%;
    background: var(--teal-light);
  }
  .brand-name {
    position: absolute; left: 0; top: 108px; width: 422px;
    text-align: center; font-weight: 300; font-size: 60px;
    line-height: 1; color: var(--teal); letter-spacing: -1px;
  }
  .section-title {
    position: absolute; left: 42px; top: 682px;
    font-weight: 800; font-size: 34px; color: var(--black); letter-spacing: 0.5px;
  }
  .title-rule {
    position: absolute; left: 44px; top: 727px; width: 307px; height: 2px;
    background: var(--rule);
  }
  .title-rule::before {
    content: ""; position: absolute; left: 0; top: -1px; width: 113px; height: 4px;
    background: var(--teal);
  }
  .values { position: absolute; top: 742px; list-style: none; }
  .values--left { left: 42px; }
  .values--right { left: 230px; top: 744px; }
  .values li {
    display: flex; align-items: center; gap: 7px;
    height: 25px; font-size: 18px; color: #2a2a2a;
  }
  .values--right li:nth-child(3) { height: 23px; }
  .values--right li:nth-child(4) { height: 27px; }
  .tick { width: 13px; height: 13px; flex: none; }
  .contact-rule {
    position: absolute; left: 40px; top: 887px; width: 330px; height: 2px;
    background: var(--rule);
  }
  .phone {
    position: absolute; left: 0; top: 898px; width: 422px; text-align: center;
    font-weight: 400; font-size: 52px; line-height: 1; color: var(--teal); letter-spacing: -2px;
  }
  .website {
    position: absolute; left: 0; top: 955px; width: 422px; text-align: center;
    font-size: 20px; color: var(--black); letter-spacing: -0.5px;
  }
</style>
</head>
<body>
<main class="canvas">
  <section class="banner" aria-label="Meridale Capital pull-up banner">
    <svg class="banner-art" viewBox="0 0 422 1045" aria-hidden="false">
      <defs>
        <linearGradient id="photoTone" x1="0" y1="0" x2="0" y2="1">
          <stop offset="0" stop-color="var(--photo-top)"/>
          <stop offset="0.28" stop-color="#e4e6e8"/>
          <stop offset="0.6" stop-color="var(--photo-mid)"/>
          <stop offset="1" stop-color="var(--photo-low)"/>
        </linearGradient>
        <linearGradient id="bandTone" x1="0" y1="0" x2="1" y2="1">
          <stop offset="0" stop-color="var(--teal-dark)"/>
          <stop offset="1" stop-color="var(--teal-light)"/>
        </linearGradient>
      </defs>
      <g role="img" aria-label="Photo of team members working together at desks with computer screens in a bright office">
        <polygon points="0,0 422,0 422,542 245,596 202,512 0,565" fill="url(#photoTone)"/>
      </g>
      <polygon points="0,565 202,512 245,596 422,542 277,653 112,590 0,695" fill="url(#bandTone)"/>
      <polygon points="245,596 422,542 277,653" fill="var(--teal-light)" opacity="0.85"/>
      <polyline points="0,563 202,510 245,594 422,540" fill="none" stroke="var(--white)" stroke-width="4"/>
      <polygon points="132,1045 160,1000 232,1045" fill="var(--teal)"/>
      <polygon points="337,1045 422,968 422,1045" fill="var(--teal)"/>
    </svg>

    <span class="brand-mark" aria-hidden="true"></span>
    <h1 class="brand-name">MERIDALE</h1>

    <h2 class="section-title">WHAT WE DO</h2>
    <div class="title-rule"></div>

    <ul class="values values--left">
      <li><svg class="tick" viewBox="0 0 14 14"><circle cx="7" cy="7" r="7" fill="var(--teal)"/><path d="M3.8 7.2l2.2 2.1 4.2-4.4" fill="none" stroke="#fff" stroke-width="1.8"/></svg>Challenging</li>
      <li><svg class="tick" viewBox="0 0 14 14"><circle cx="7" cy="7" r="7" fill="var(--teal)"/><path d="M3.8 7.2l2.2 2.1 4.2-4.4" fill="none" stroke="#fff" stroke-width="1.8"/></svg>Rewarding</li>
      <li><svg class="tick" viewBox="0 0 14 14"><circle cx="7" cy="7" r="7" fill="var(--teal)"/><path d="M3.8 7.2l2.2 2.1 4.2-4.4" fill="none" stroke="#fff" stroke-width="1.8"/></svg>Passionate</li>
      <li><svg class="tick" viewBox="0 0 14 14"><circle cx="7" cy="7" r="7" fill="var(--teal)"/><path d="M3.8 7.2l2.2 2.1 4.2-4.4" fill="none" stroke="#fff" stroke-width="1.8"/></svg>Entrepreneurial</li>
      <li><svg class="tick" viewBox="0 0 14 14"><circle cx="7" cy="7" r="7" fill="var(--teal)"/><path d="M3.8 7.2l2.2 2.1 4.2-4.4" fill="none" stroke="#fff" stroke-width="1.8"/></svg>Focused</li>
    </ul>
    <ul class="values values--right">
      <li><svg class="tick" viewBox="0 0 14 14"><circle cx="7" cy="7" r="7" fill="var(--teal)"/><path d="M3.8 7.2l2.2 2.1 4.2-4.4" fill="none" stroke="#fff" stroke-width="1.8"/></svg>Collaborative</li>
      <li><svg class="tick" viewBox="0 0 14 14"><circle cx="7" cy="7" r="7" fill="var(--teal)"/><path d="M3.8 7.2l2.2 2.1 4.2-4.4" fill="none" stroke="#fff" stroke-width="1.8"/></svg>Innovative</li>
      <li><svg class="tick" viewBox="0 0 14 14"><circle cx="7" cy="7" r="7" fill="var(--teal)"/><path d="M3.8 7.2l2.2 2.1 4.2-4.4" fill="none" stroke="#fff" stroke-width="1.8"/></svg>Systematic</li>
      <li><svg class="tick" viewBox="0 0 14 14"><circle cx="7" cy="7" r="7" fill="var(--teal)"/><path d="M3.8 7.2l2.2 2.1 4.2-4.4" fill="none" stroke="#fff" stroke-width="1.8"/></svg>Strategic</li>
    </ul>

    <div class="contact-rule"></div>
    <p class="phone">0198-765-432</p>
    <p class="website">www.meridalecapital.com.au</p>
  </section>
</main>
</body>
</html>
```